Book about Ice Dragons

I would like a book cover made for my book i am planning on releasing soon, the book is title "Corvath: DUSK", i would like a white background with the words Corvath: DUSK in the middle with some sort of dragon medallion / logo in the middle, i would love the wording to have a subtle ice effect, on the back i want a small picture at the top with a a dragon perched on a rock with a man standing below the dragon, I want the dragon to dwarf the man, I like the stronger dinosaur like dragons not the Chinese style. I really like the way the dragon looks in the attached picture but i'm not a fan of the whiskers on the dragons face.

```html
<!DOCTYPE html>
<html lang="en">
<head>
<meta charset="UTF-8">
<title>Corvath: DUSK — Book Cover</title>
<link href="https://fonts.googleapis.com/css2?family=Bebas+Neue&display=swap" rel="stylesheet">
<style>
  :root {
    --frost-white: #f5f8fa;
    --frost-grey: #dfe7ec;
    --frost-shadow: #c6d3db;
    --frost-scratch: #aebfca;
    --title-blue: #3f9fd3;
    --title-blue-light: #9fd6f0;
    --shield-deep: #1b4a82;
    --shield-mid: #2d68a4;
    --shield-light: #5d8fc1;
    --plank-line: rgba(10, 30, 60, 0.45);
    --rim-silver: #e9eef2;
    --rim-edge: #9aa6ae;
    --glow: rgba(150, 205, 235, 0.8);
    --emblem-white: #f2f6fa;
  }
  * { margin: 0; padding: 0; box-sizing: border-box; }
  html, body { width: 750px; height: 1200px; overflow: hidden; }
  body { background: var(--frost-white); }
  .cover {
    position: relative;
    width: 750px;
    height: 1200px;
    overflow: hidden;
  }
  .cover-art {
    position: absolute;
    inset: 0;
    width: 750px;
    height: 1200px;
  }
  .title-text {
    font-family: "Bebas Neue", "Arial Narrow", sans-serif;
    text-anchor: middle;
  }
  .title-name { font-size: 172px; letter-spacing: 15px; }
  .title-sub { font-size: 292px; letter-spacing: 18px; }
  .medallion {
    position: absolute;
    left: 112px;
    top: 560px;
    width: 530px;
    height: 570px;
    filter: drop-shadow(0 0 20px var(--glow));
  }
</style>
</head>
<body>
  <main class="cover">
    <svg class="cover-art" viewBox="0 0 750 1200" xmlns="http://www.w3.org/2000/svg">
      <defs>
        <radialGradient id="frost-base" cx="0.5" cy="0.45" r="0.75">
          <stop offset="0" stop-color="var(--frost-white)"/>
          <stop offset="0.45" stop-color="var(--frost-white)"/>
          <stop offset="1" stop-color="var(--frost-shadow)"/>
        </radialGradient>
        <linearGradient id="title-fill" x1="0" y1="0" x2="0" y2="1">
          <stop offset="0" stop-color="var(--title-blue)"/>
          <stop offset="1" stop-color="var(--title-blue-light)"/>
        </linearGradient>

        <filter id="frost-grain" x="0" y="0" width="100%" height="100%">
          <feTurbulence type="fractalNoise" baseFrequency="0.012" numOctaves="4" seed="3" result="cloud"/>
          <feColorMatrix in="cloud" type="matrix"
            values="0 0 0 0 0.68  0 0 0 0 0.75  0 0 0 0 0.8  0 0 0 -1.6 1.0" result="cloudTint"/>
          <feTurbulence type="fractalNoise" baseFrequency="0.9" numOctaves="2" seed="8" result="grain"/>
          <feColorMatrix in="grain" type="matrix"
            values="0 0 0 0 0.6  0 0 0 0 0.68  0 0 0 0 0.74  0 0 0 -3 1.55" result="grainTint"/>
          <feMerge>
            <feMergeNode in="cloudTint"/>
            <feMergeNode in="grainTint"/>
          </feMerge>
        </filter>

        <filter id="frost-scratches" x="0" y="0" width="100%" height="100%">
          <feTurbulence type="fractalNoise" baseFrequency="0.003 0.09" numOctaves="3" seed="11" result="streak"/>
          <feColorMatrix in="streak" type="matrix"
            values="0 0 0 0 0.62  0 0 0 0 0.7  0 0 0 0 0.77  0 0 0 -5 2.6"/>
        </filter>

        <filter id="ice-distress" x="-5%" y="-10%" width="110%" height="120%">
          <feTurbulence type="fractalNoise" baseFrequency="0.05" numOctaves="2" seed="4" result="warp"/>
          <feDisplacementMap in="SourceGraphic" in2="warp" scale="5" xChannelSelector="R" yChannelSelector="G" result="ragged"/>
          <feTurbulence type="fractalNoise" baseFrequency="0.75" numOctaves="2" seed="6" result="pits"/>
          <feColorMatrix in="pits" type="matrix"
            values="0 0 0 0 0  0 0 0 0 0  0 0 0 0 0  0 0 0 -2.6 2.05" result="pitMask"/>
          <feTurbulence type="fractalNoise" baseFrequency="0.006 0.12" numOctaves="2" seed="2" result="cracks"/>
          <feColorMatrix in="cracks" type="matrix"
            values="0 0 0 0 0  0 0 0 0 0  0 0 0 0 0  0 0 0 -6 3.7" result="crackMask"/>
          <feComposite in="pitMask" in2="crackMask" operator="in" result="wearMask"/>
          <feComposite in="ragged" in2="wearMask" operator="in" result="worn"/>
          <feTurbulence type="fractalNoise" baseFrequency="0.04" numOctaves="3" seed="9" result="shade"/>
          <feColorMatrix in="shade" type="matrix"
            values="0 0 0 0 1  0 0 0 0 1  0 0 0 0 1  0 0 0 -1.8 0.9" result="frostSheen"/>
          <feComposite in="frostSheen" in2="worn" operator="in" result="sheenOnText"/>
          <feMerge>
            <feMergeNode in="worn"/>
            <feMergeNode in="sheenOnText"/>
          </feMerge>
        </filter>
      </defs>

      <rect class="frost-base" width="750" height="1200" fill="url(#frost-base)"/>
      <rect class="frost-grain" width="750" height="1200" filter="url(#frost-grain)" opacity="0.55"/>
      <rect class="frost-scratches" width="750" height="1200" filter="url(#frost-scratches)" opacity="0.45"
            transform="rotate(-20 375 600) translate(-300 -300) scale(1.8)"/>

      <g class="title" fill="url(#title-fill)" filter="url(#ice-distress)">
        <text class="title-text title-name" x="383" y="208">Corvath:</text>
        <text class="title-text title-sub" x="384" y="468">DUSK</text>
      </g>
    </svg>

    <svg class="medallion" viewBox="0 0 530 570" xmlns="http://www.w3.org/2000/svg">
      <defs>
        <linearGradient id="shield-fill" x1="0" y1="0" x2="0" y2="1">
          <stop offset="0" stop-color="var(--shield-deep)"/>
          <stop offset="0.55" stop-color="var(--shield-mid)"/>
          <stop offset="1" stop-color="var(--shield-light)"/>
        </linearGradient>
        <linearGradient id="rim-fill" x1="0" y1="0" x2="1" y2="1">
          <stop offset="0" stop-color="var(--rim-silver)"/>
          <stop offset="0.5" stop-color="#ffffff"/>
          <stop offset="1" stop-color="var(--rim-edge)"/>
        </linearGradient>
        <radialGradient id="emblem-fill" cx="0.5" cy="0.5" r="0.6">
          <stop offset="0" stop-color="var(--emblem-white)" stop-opacity="0.95"/>
          <stop offset="1" stop-color="var(--emblem-white)" stop-opacity="0.7"/>
        </radialGradient>
        <filter id="shield-mottle" x="0" y="0" width="100%" height="100%">
          <feTurbulence type="fractalNoise" baseFrequency="0.02" numOctaves="4" seed="5"/>
          <feColorMatrix type="matrix"
            values="0 0 0 0 0.85  0 0 0 0 0.92  0 0 0 0 1  0 0 0 -1.4 0.75"/>
        </filter>
        <clipPath id="shield-inner">
          <path d="M30 48 Q265 14 500 48 L500 255 Q488 410 265 538 Q42 410 30 255 Z"/>
        </clipPath>
      </defs>

      <path class="shield-rim" d="M8 34 Q265 -6 522 34 L522 258 Q508 430 265 566 Q22 430 8 258 Z"
            fill="url(#rim-fill)" stroke="var(--rim-edge)" stroke-width="2"/>
      <path class="shield-face" d="M30 48 Q265 14 500 48 L500 255 Q488 410 265 538 Q42 410 30 255 Z"
            fill="url(#shield-fill)"/>
      <rect class="shield-frost" width="530" height="570" clip-path="url(#shield-inner)"
            filter="url(#shield-mottle)" opacity="0.35"/>

      <g class="shield-planks" clip-path="url(#shield-inner)" stroke="var(--plank-line)" stroke-width="3">
        <line x1="0" y1="78" x2="530" y2="78"/>
        <line x1="0" y1="118" x2="530" y2="118"/>
        <line x1="0" y1="158" x2="530" y2="158"/>
        <line x1="0" y1="198" x2="530" y2="198"/>
        <line x1="0" y1="238" x2="530" y2="238"/>
        <line x1="0" y1="278" x2="530" y2="278"/>
        <line x1="0" y1="318" x2="530" y2="318"/>
        <line x1="0" y1="358" x2="530" y2="358"/>
        <line x1="0" y1="398" x2="530" y2="398"/>
        <line x1="0" y1="438" x2="530" y2="438"/>
        <line x1="0" y1="478" x2="530" y2="478"/>
      </g>

      <rect class="dragon-emblem" x="138" y="62" width="262" height="318" rx="60"
            fill="url(#emblem-fill)"
            role="img" aria-label="White rearing dragon emblem with spread wing and curled tail"/>
    </svg>
  </main>
</body>
</html>
```